Web design for a website of car care products and facility management

I need someone who can do the graphic design for a website of car care products and facility management. We will need the design of the homepage with the "About Us", "Services", Product's Catalog", "Team" and "Contact Us".
-Attached you will find our profile.
-We don’t have images, we can get them from free bank images
-We would like to be able to write things later on, so the designer only has to do the text on the homepage with the main links to “About Us”, etc.
-We would like to get a suggestion from the designer to where is best to host our website.
Target Market(s)
Our buyers are B2B companies
Number of Pages Required
5+ page
Look and feel
Each slider illustrates characteristics of the customer's brand and the style your logo design should communicate.

```html
<!DOCTYPE html>
<html lang="en">
<head>
<meta charset="utf-8">
<title>Northway Trading – Products Catalog</title>
<link href="https://fonts.googleapis.com/css2?family=Sorts+Mill+Goudy:ital@0;1&display=swap" rel="stylesheet">
<style>
:root{
  --red:#c1272d;
  --ink:#2b2b2b;
  --muted:#8a8a8a;
  --page:#f2f2f2;
  --topbar:#f6f6f6;
  --white:#ffffff;
  --card:#fbfaf8;
  --rule:#d4d4d4;
  --icon:#3a3a3a;
}
*{margin:0;padding:0;box-sizing:border-box}
html,body{width:910px;height:1200px;overflow:hidden}
body{position:relative;background:var(--page);font-family:"Sorts Mill Goudy",Georgia,serif;color:var(--ink)}
.abs{position:absolute}
.topbar{left:0;top:0;width:910px;height:22px;background:var(--topbar)}
.contact-item{top:4px;font-size:8.5px;display:flex;align-items:center;gap:5px;letter-spacing:.3px}
.social-top{right:175px;top:4px;display:flex;gap:8px}
.dot{width:14px;height:14px;border-radius:50%;background:var(--icon)}
.header{left:0;top:22px;width:910px;height:73px;background:var(--white)}
.brand{left:175px;top:44px;font-size:14px;color:var(--red);display:flex;align-items:center;gap:6px;line-height:1}
.brand .mark{width:16px;height:16px;background:var(--red)}
.nav{left:296px;top:52px;display:flex;gap:12px;font-size:8.6px;letter-spacing:.4px}
.nav .active{color:var(--red)}
.page-title{left:174px;top:113px;font-size:23px;font-weight:normal;color:var(--red);letter-spacing:1.6px;line-height:1}
.search{left:407px;top:118px;width:329px;height:19px;border:1px solid #cfcfcf;border-radius:4px;background:#ececec;display:flex;overflow:hidden}
.search .cat{width:75px;background:var(--red);color:#fff;font-size:8.5px;display:flex;align-items:center;justify-content:center}
.search .field{flex:1;font-size:8.5px;padding-left:9px;display:flex;align-items:center}
.search svg{margin:auto 8px}
.sidebar{left:175px;top:165px;width:114px;height:180px;background:var(--white);border-radius:5px;padding:14px 10px}
.sidebar h3{font-weight:normal;font-size:10px;color:var(--red);letter-spacing:.5px;margin-bottom:8px}
.sidebar li{list-style:none;font-size:8px;line-height:11.9px}
.sidebar li.current{color:var(--red)}
.section-title{left:297px;top:163px;font-size:13px;font-weight:normal;color:var(--red);letter-spacing:1px}
.section-rule{left:297px;top:183px;width:438px;height:2px;background:var(--rule)}
.sort{left:296px;top:191px;width:80px;height:16px;background:var(--red);border-radius:3px;color:#fff;font-size:8px;display:flex;align-items:center;justify-content:center}
.pager{font-size:8px;color:var(--muted);letter-spacing:.3px}
.pager b{font-weight:normal;color:var(--red)}
.grid{left:296px;top:227px;width:440px;display:grid;grid-template-columns:repeat(4,101px);column-gap:12.3px;row-gap:19px}
.card .img{height:118px;border-radius:4px;background:var(--card);box-shadow:0 0 3px rgba(0,0,0,.07);position:relative;overflow:hidden}
.card .img::after{content:"";position:absolute;left:50%;top:50%;transform:translate(-50%,-50%);border-radius:40%;filter:blur(6px)}
.compressor .img::after{width:66px;height:62px;background:radial-gradient(circle,#3a3a3a 0%,#555 55%,rgba(80,80,80,0) 100%)}
.wrench .img::after{width:34px;height:76px;background:radial-gradient(circle,#9a9a9a 0%,#c4c4c4 60%,rgba(200,200,200,0) 100%)}
.bottle .img::after{width:26px;height:80px;border-radius:30%;background:radial-gradient(circle,#ff7a2e 0%,#ff8a3d 60%,rgba(255,140,60,0) 100%)}
.powder .img::after{width:80px;height:40px;background:radial-gradient(circle,#d9dedc 0%,#b9cfc9 55%,rgba(190,210,205,0) 100%)}
.battery .img::after{width:66px;height:56px;background:radial-gradient(circle,#2f4a8a 0%,#222 55%,rgba(40,40,40,0) 100%)}
.cleaning .img::after{width:70px;height:72px;background:radial-gradient(circle,#f08a2c 0%,#e05a9a 45%,#2c5fb0 70%,rgba(60,90,170,0) 100%)}
.roller .img::after{width:80px;height:58px;background:linear-gradient(135deg,rgba(200,140,80,0) 5%,#c98a55 30%,#bdbdbd 60%,#eee 80%,rgba(240,240,240,0) 95%)}
.card .name{font-size:9px;margin-top:5px;letter-spacing:.4px;line-height:11px}
.card .desc{font-size:9px;color:var(--muted);letter-spacing:.4px;line-height:11px}
.footer{left:0;top:945px;width:910px;height:255px;background:linear-gradient(180deg,#2c2c2c 0%,#333 55%,#232323 100%)}
.foot-brand{left:128px;top:1010px;font-size:18px;color:var(--red);display:flex;align-items:center;gap:7px}
.foot-brand .mark{width:20px;height:20px;background:var(--red)}
.copyright{left:128px;top:1082px;font-size:9px;color:#fff;line-height:14px;letter-spacing:.3px}
.foot-h{font-style:italic;font-size:14px;color:var(--red);letter-spacing:.8px}
.sitemap{left:278px;top:1027px;color:#fff;font-size:10px;line-height:20.8px;letter-spacing:.5px}
.info{left:421px;top:1027px;color:#fff;font-size:10px;line-height:21px;letter-spacing:.3px}
.info .row{display:flex;gap:8px;align-items:flex-start}
.info .ic{width:16px;flex:none;display:flex;justify-content:center;padding-top:4px}
.partner{left:645px;top:1022px;font-size:20px;color:#f06b22;letter-spacing:1px}
.social-foot{left:645px;top:1105px;display:flex;gap:7px}
.social-foot .dot{width:20px;height:20px;background:#6a6a6a}
</style>
</head>
<body>
<div class="abs topbar"></div>
<div class="abs contact-item" style="left:175px">
  <svg width="14" height="14" viewBox="0 0 14 14"><circle cx="7" cy="7" r="7" fill="var(--icon)"/><path d="M4.6 3.8l1.3-.2.7 1.7-.8.6c.4.9 1 1.5 1.9 1.9l.6-.8 1.7.7-.2 1.3c-3 .2-5.4-2.2-5.2-5.2z" fill="#fff"/></svg>
  +966 50 000 4127</div>
<div class="abs contact-item" style="left:277px">
  <svg width="14" height="14" viewBox="0 0 14 14"><circle cx="7" cy="7" r="7" fill="var(--icon)"/><rect x="3.8" y="4.8" width="6.4" height="4.4" rx=".6" fill="none" stroke="#fff" stroke-width=".9"/><path d="M4 5.1l3 2.2 3-2.2" fill="none" stroke="#fff" stroke-width=".9"/></svg>
  info@northway-trade.sa</div>
<div class="abs social-top"><span class="dot"></span><span class="dot"></span><span class="dot"></span><span class="dot"></span><span class="dot"></span><span class="dot"></span></div>

<div class="abs header"></div>
<div class="abs brand"><span class="mark"></span>Northway</div>
<nav class="abs nav"><span>ABOUT US</span><span>SERVICES</span><span>OUR PARTNER</span><span class="active">PRODUCTS CATALOG</span><span>CUSTOMER REVIEWS</span><span>CONTACT US</span></nav>

<h1 class="abs page-title">OUR PRODUCTS</h1>
<div class="abs search">
  <div class="cat">All Categories ▾</div>
  <div class="field">Search</div>
  <svg width="11" height="11" viewBox="0 0 11 11"><circle cx="4.5" cy="4.5" r="3.4" fill="none" stroke="var(--ink)" stroke-width="1.5"/><path d="M7 7l3 3" stroke="var(--ink)" stroke-width="1.6"/></svg>
</div>

<aside class="abs sidebar">
  <h3>CATEGORIES</h3>
  <ul>
    <li class="current">- Equipment (44)</li>
    <li>- Tools (104)</li>
    <li>- Polishing Items (65)</li>
    <li>- Additivess (50)</li>
    <li>- Batteries (20)</li>
    <li>- Cleaning Items (70)</li>
    <li>- Painting Materials (94)</li>
  </ul>
</aside>

<h2 class="abs section-title">CHEMICALS</h2>
<div class="abs section-rule"></div>
<div class="abs sort">Sort by: Newest ▾</div>
<div class="abs pager" style="right:177px;top:194px"><b>1,</b> 2, 3, 4... <b>&gt;&gt;</b></div>

<div class="abs grid">
  <div class="card compressor"><div class="img" role="img" aria-label="Air compressor product photo"></div><div class="name">Product Name</div><div class="desc">Short Description</div></div>
  <div class="card wrench"><div class="img" role="img" aria-label="Wrench tools product photo"></div><div class="name">Product Name</div><div class="desc">Short Description</div></div>
  <div class="card bottle"><div class="img" role="img" aria-label="Orange chemical bottle product photo"></div><div class="name">Product Name</div><div class="desc">Short Description</div></div>
  <div class="card powder"><div class="img" role="img" aria-label="White powder additive product photo"></div><div class="name">Product Name</div><div class="desc">Short Description</div></div>

  <div class="card battery"><div class="img" role="img" aria-label="Car battery product photo"></div><div class="name">Product Name</div><div class="desc">Short Description</div></div>
  <div class="card cleaning"><div class="img" role="img" aria-label="Cleaning supplies bucket product photo"></div><div class="name">Product Name</div><div class="desc">Short Description</div></div>
  <div class="card roller"><div class="img" role="img" aria-label="Paint roller product photo"></div><div class="name">Product Name</div><div class="desc">Short Description</div></div>
  <div class="card powder"><div class="img" role="img" aria-label="White powder additive product photo"></div><div class="name">Product Name</div><div class="desc">Short Description</div></div>

  <div class="card compressor"><div class="img" role="img" aria-label="Air compressor product photo"></div><div class="name">Product Name</div><div class="desc">Short Description</div></div>
  <div class="card wrench"><div class="img" role="img" aria-label="Wrench tools product photo"></div><div class="name">Product Name</div><div class="desc">Short Description</div></div>
  <div class="card bottle"><div class="img" role="img" aria-label="Orange chemical bottle product photo"></div><div class="name">Product Name</div><div class="desc">Short Description</div></div>
  <div class="card powder"><div class="img" role="img" aria-label="White powder additive product photo"></div><div class="name">Product Name</div><div class="desc">Short Description</div></div>

  <div class="card battery"><div class="img" role="img" aria-label="Car battery product photo"></div><div class="name">Product Name</div><div class="desc">Short Description</div></div>
  <div class="card cleaning"><div class="img" role="img" aria-label="Cleaning supplies bucket product photo"></div><div class="name">Product Name</div><div class="desc">Short Description</div></div>
  <div class="card roller"><div class="img" role="img" aria-label="Paint roller product photo"></div><div class="name">Product Name</div><div class="desc">Short Description</div></div>
  <div class="card powder"><div class="img" role="img" aria-label="White powder additive product photo"></div><div class="name">Product Name</div><div class="desc">Short Description</div></div>
</div>

<div class="abs pager" style="right:177px;top:880px"><b>1,</b> 2, 3, 4... <b>&gt;&gt;</b></div>

<footer class="abs footer" role="img" aria-label="Dark background photo of a sports car"></footer>
<div class="abs foot-brand"><span class="mark"></span>Northway</div>
<div class="abs copyright">©2023 All Rights Reserved<br>Northway Trading Company</div>

<div class="abs foot-h" style="left:278px;top:991px">SITEMAP</div>
<div class="abs sitemap">ABOUT US<br>SERVICES<br>OUR PARTNER<br>PRODUCTS CATALOG<br>CUSTOMER REVIEWS<br>CONTACT US</div>

<div class="abs foot-h" style="left:421px;top:991px">CONTACT INFO</div>
<div class="abs info">
  <div class="row"><span class="ic"><svg width="14" height="14" viewBox="0 0 14 14"><circle cx="7" cy="7" r="7" fill="var(--red)"/><path d="M7 3.3a2.4 2.4 0 0 1 2.4 2.4c0 1.8-2.4 4.6-2.4 4.6S4.6 7.5 4.6 5.7A2.4 2.4 0 0 1 7 3.3z" fill="#fff"/><circle cx="7" cy="5.7" r=".9" fill="var(--red)"/></svg></span><span>12 Al Noor St, Harbor Rd.<br>Al Salam Plaza Center. Al Rawdah<br>Jeddah 21400. Floor 2, Office 208</span></div>
  <div class="row"><span class="ic"><svg width="14" height="14" viewBox="0 0 14 14"><circle cx="7" cy="7" r="7" fill="var(--red)"/><path d="M4.6 3.8l1.3-.2.7 1.7-.8.6c.4.9 1 1.5 1.9 1.9l.6-.8 1.7.7-.2 1.3c-3 .2-5.4-2.2-5.2-5.2z" fill="#fff"/></svg></span><span>+966 50 000 4127</span></div>
  <div class="row"><span class="ic"><svg width="14" height="14" viewBox="0 0 14 14"><circle cx="7" cy="7" r="7" fill="var(--red)"/><rect x="3.8" y="4.8" width="6.4" height="4.4" rx=".6" fill="none" stroke="#fff" stroke-width=".9"/><path d="M4 5.1l3 2.2 3-2.2" fill="none" stroke="#fff" stroke-width=".9"/></svg></span><span>info@northway-trade.sa</span></div>
  <div class="row"><span class="ic"><svg width="14" height="14" viewBox="0 0 14 14"><circle cx="7" cy="7" r="7" fill="var(--red)"/><circle cx="7" cy="7" r="3.3" fill="none" stroke="#fff" stroke-width=".8"/><path d="M3.7 7h6.6M7 3.7c-1.6 2-1.6 4.6 0 6.6M7 3.7c1.6 2 1.6 4.6 0 6.6" fill="none" stroke="#fff" stroke-width=".7"/></svg></span><span>www.northway-trade.sa</span></div>
</div>

<div class="abs foot-h" style="left:645px;top:991px">BUSINESS PARTNERS</div>
<div class="abs partner">Brightline</div>
<div class="abs foot-h" style="left:645px;top:1079px">FOLLOW US</div>
<div class="abs social-foot"><span class="dot"></span><span class="dot"></span><span class="dot"></span><span class="dot"></span><span class="dot"></span><span class="dot"></span></div>
</body>
</html>
```